この度、「名刺デザイン」の作成をお願いいたします。
ターゲット顧客としては20~40代女性をメインとしています。
ロゴもスマイルをモチーフとしたデザインのため、固くなりすぎない、ちょっと遊び心のあるデザインをいただけると嬉しいです。
表面:事業所名・屋号・役職・氏名・住所・電話番号・メールアドレス・顔写真(可能であれば)
裏面:なし
シンプル 複雑
単色 カラフル
暗い 明るい
日常 高級
遊び心 厳粛
未来的 伝統的
女性的 男性的
水色系
• 高解像度JPG (.jpg)
• イラストレーター形式 (.ai)
• フォトショップ形式 (.psd)
• PNG形式 (.png)

全体的名デザインの雰囲気とがよく、裏面のデザインが面白かったので採用させていただきました。

今回はビジネス名詞でありながら、遊び心や可愛さを求めるというご依頼でありましたが、50件を越えるご提案をいただき本当にありがとうございました。
数も多く、どれも選び難いデザインだったため、当選までにお日にちがかかってしまったことはお詫び申し上げます。
また何かご依頼をさせていただくこともあるかと思いますが、是非またよろしくお願いいたします。

```html
<!DOCTYPE html>
<html lang="ja">
<head>
<meta charset="utf-8">
<title>CARJOY 名刺</title>
<link rel="stylesheet" href="https://fonts.googleapis.com/css2?family=M+PLUS+Rounded+1c:wght@400;500;700;800&display=swap">
<style>
  :root {
    --sky: #38a9e6;
    --sky-deep: #1f8fd3;
    --sky-soft: #bfe3f7;
    --ink: #333a40;
    --muted: #5a6670;
    --paper: #ffffff;
  }
  * { margin: 0; padding: 0; box-sizing: border-box; }
  html, body { width: 781px; height: 1200px; overflow: hidden; background: var(--paper); }
  body { font-family: "M PLUS Rounded 1c", sans-serif; color: var(--ink); }
  .card { position: relative; width: 781px; height: 1200px; overflow: hidden; background: var(--paper); }
  .card__waves { position: absolute; inset: 0; }
  .brand { position: absolute; top: 140px; left: 0; width: 100%; text-align: center; color: var(--paper); }
  .brand__name { font-size: 104px; font-weight: 800; letter-spacing: 10px; line-height: 1; }
  .brand__tagline { margin-top: 14px; font-size: 34px; font-weight: 500; letter-spacing: 6px; }
  .person { position: absolute; top: 520px; left: 65px; width: 400px; }
  .person__role { color: var(--sky-deep); font-size: 34px; font-weight: 700; line-height: 1.2; }
  .person__name { margin-top: 6px; font-size: 66px; font-weight: 500; letter-spacing: 4px; line-height: 1.2; }
  .person__roman { margin-top: 4px; color: var(--muted); font-size: 32px; line-height: 1.2; }
  .person__rule { margin-top: 14px; height: 4px; width: 390px; background: var(--sky); border-radius: 2px; }
  .portrait { position: absolute; top: 455px; left: 455px; width: 280px; height: 280px; border-radius: 50%;
    border: 6px solid var(--sky); padding: 6px; background: var(--paper); }
  .portrait__fill { width: 100%; height: 100%; border-radius: 50%;
    background: linear-gradient(180deg, #e9eef2 0%, #c9d3db 55%, #4c5661 100%); }
  .contact { position: absolute; top: 768px; left: 70px; list-style: none; }
  .contact__item { display: flex; align-items: center; gap: 14px; font-size: 30px; color: var(--muted); line-height: 1.25; }
  .contact__item + .contact__item { margin-top: 16px; }
  .contact__item--company { color: var(--sky-deep); font-size: 36px; font-weight: 500; }
  .contact__icon { width: 38px; height: 38px; flex: none; }
  .contact__address { display: block; }
  .vehicle { position: absolute; top: 1052px; left: 600px; width: 130px; height: 54px;
    border-radius: 28px 34px 8px 8px; background: var(--sky-soft); }
</style>
</head>
<body>
<main class="card">
  <svg class="card__waves" width="781" height="1200" viewBox="0 0 781 1200" aria-hidden="true">
    <path d="M0 0 H781 V520 C620 470 420 420 220 440 C120 450 50 470 0 490 Z" fill="var(--sky)"/>
    <path d="M0 470 C80 440 200 420 300 425" fill="none" stroke="var(--paper)" stroke-width="4" opacity="0.6"/>
    <path d="M0 1170 C220 1140 520 1135 781 1160 V1200 H0 Z" fill="var(--sky)"/>
    <path d="M0 1148 C220 1118 520 1108 781 1132" fill="none" stroke="var(--sky)" stroke-width="4"/>
  </svg>

  <header class="brand">
    <div class="brand__name">CARJOY</div>
    <div class="brand__tagline">自動車販売・レンタカー</div>
  </header>

  <section class="person">
    <p class="person__role">代 表</p>
    <h1 class="person__name">山田 花子</h1>
    <p class="person__roman">Hanako Yamada</p>
    <div class="person__rule"></div>
  </section>

  <div class="portrait"><div class="portrait__fill" role="img" aria-label="代表者の顔写真"></div></div>

  <ul class="contact">
    <li class="contact__item">
      <svg class="contact__icon" viewBox="0 0 40 40" aria-hidden="true"><circle cx="20" cy="20" r="18" fill="none" stroke="var(--sky)" stroke-width="3"/><rect x="14" y="9" width="12" height="22" rx="2" fill="var(--sky)"/></svg>
      080-0000-1111
    </li>
    <li class="contact__item contact__item--company">
      <svg class="contact__icon" viewBox="0 0 40 40" aria-hidden="true"><circle cx="20" cy="20" r="18" fill="none" stroke="var(--sky)" stroke-width="3"/><rect x="12" y="11" width="16" height="19" fill="var(--sky)"/></svg>
      株式会社HIKARI
    </li>
    <li class="contact__item">
      <svg class="contact__icon" viewBox="0 0 40 40" aria-hidden="true"><circle cx="20" cy="20" r="18" fill="none" stroke="var(--sky)" stroke-width="3"/><path d="M20 31 C12 22 12 18 12 16 A8 8 0 0 1 28 16 C28 18 28 22 20 31 Z" fill="var(--sky)"/><circle cx="20" cy="16" r="3" fill="var(--paper)"/></svg>
      <span><span class="contact__address">〒100-0000</span><span class="contact__address">東京都港区00000-000</span></span>
    </li>
    <li class="contact__item">
      <svg class="contact__icon" viewBox="0 0 40 40" aria-hidden="true"><circle cx="20" cy="20" r="18" fill="none" stroke="var(--sky)" stroke-width="3"/><path d="M13 11 L17 11 L19 16 L16 18 C17 21 19 23 22 24 L24 21 L29 23 L29 27 C20 28 12 20 13 11 Z" fill="var(--sky)"/></svg>
      03-000-1111
    </li>
    <li class="contact__item">
      <svg class="contact__icon" viewBox="0 0 40 40" aria-hidden="true"><circle cx="20" cy="20" r="18" fill="none" stroke="var(--sky)" stroke-width="3"/><rect x="10" y="13" width="20" height="14" rx="2" fill="var(--sky)"/><path d="M10 14 L20 22 L30 14" fill="none" stroke="var(--paper)" stroke-width="2"/></svg>
      info@carjoy.example
    </li>
  </ul>

  <div class="vehicle" role="img" aria-label="水色の車のイラスト"></div>
</main>
</body>
</html>
```